Prepared ready to cook meal delivery service needs a flyer design

We need a flyer design for a startup company based in Cape Town, South Africa. I've attached a few flyer designs that I like.

The company is called 'Pemblo' and our website will be found at pemblo.co.za. We don't have a logo yet.

Flyer text:

Pemblo
Simply sizzle

Do you feel like a home cooked meal but don't like shopping, peeling, chopping, cooking, or cleaning up?

We deliver ready to roast free range chicken and fresh vegetables to your door.

To order: SMS your name to 074 318 6149 and we'll call you back.

Only the best ingredients used
Free range chickens. Fresh herbs and vegetables. Virgin olive oil.

No bad carbs!

Ready to roast Free range chicken and fresh veggies
For 2 R99
For 4 R139
Updates

Wording of flyer updated.

Target Market(s)

Local Cape Townians that hate grocery shopping and need help saving time preparing meals.

Industry/Entity Type

Delivery Service

Requirements
Must have
• To find out more: SMS your name to 074 318 6149

```html
<!DOCTYPE html>
<html lang="en">
<head>
<meta charset="utf-8">
<title>Pemblo – Flyer</title>
<link rel="stylesheet" href="https://fonts.googleapis.com/css2?family=Montserrat:wght@700;800&family=Questrial&display=swap">
<style>
  :root {
    --page-bg: #e9e9e9;
    --flyer-black: #0d0d0d;
    --flyer-dark: #1c1c1c;
    --banner-red: #e0241b;
    --accent-yellow: #f4e20f;
    --text-white: #ffffff;
    --text-grey: #d6d6d6;
    --ink: #111111;
  }
  * { box-sizing: border-box; margin: 0; padding: 0; }
  html, body {
    width: 1200px; height: 1000px; overflow: hidden;
    background: var(--page-bg);
  }
  .flyer {
    position: absolute; left: 100px; top: 160px;
    width: 1000px; height: 680px;
    background: linear-gradient(160deg, var(--flyer-dark), var(--flyer-black) 60%);
    overflow: hidden;
    font-family: "Questrial", sans-serif;
    color: var(--text-white);
    box-shadow: 0 6px 18px rgba(0,0,0,.25);
  }
  .yellow-band { position: absolute; left: 0; top: 0; width: 1000px; height: 680px; }
  .headline-banner {
    position: absolute; left: 330px; top: 24px; right: 0; height: 78px;
    background: var(--banner-red);
    padding: 8px 0 0 34px;
    text-transform: uppercase;
  }
  .headline-banner .question {
    font-family: "Montserrat", sans-serif; font-weight: 800;
    font-size: 36px; line-height: 1; letter-spacing: .5px;
  }
  .headline-banner .answer { font-size: 25px; line-height: 1.2; margin-top: 4px; }
  .oven-visual {
    position: absolute; left: 40px; top: 40px; width: 400px; height: 400px;
    background: linear-gradient(180deg, #6b6b6b 0%, #2a2a2a 45%, #3a3a3a 75%, #151515 100%);
    border: 2px solid #4a4a4a;
  }
  .brand {
    position: absolute; left: 40px; top: 170px; width: 400px;
    text-align: center;
    font-family: "Montserrat", sans-serif; font-weight: 800;
    color: var(--text-white);
  }
  .brand .name { font-size: 64px; line-height: 1; }
  .brand .tagline { font-size: 34px; line-height: 1.2; text-transform: uppercase; }
  .dish-photo {
    position: absolute; left: 610px; top: 118px; width: 370px; height: 200px;
    background: #ffffff; padding: 10px;
  }
  .dish-photo .fill {
    width: 100%; height: 100%;
    background: radial-gradient(ellipse at 55% 45%, #d9a24a 0%, #b56d2a 40%, #b8262a 70%, #6a8a3a 100%);
  }
  .intro {
    position: absolute; left: 560px; top: 336px; width: 420px;
    font-size: 17px; line-height: 1.3; color: var(--text-grey);
  }
  .no-carbs {
    position: absolute; left: 520px; top: 410px;
    font-family: "Montserrat", sans-serif; font-weight: 800; font-size: 28px;
  }
  .offer {
    position: absolute; left: 520px; top: 452px;
    font-size: 17px; color: var(--text-grey);
  }
  .price {
    position: absolute;
    font-family: "Montserrat", sans-serif; font-weight: 700; font-size: 24px;
  }
  .price-two { left: 500px; top: 486px; }
  .price-four { left: 820px; top: 500px; }
  .ingredients {
    position: absolute; left: 30px; top: 468px; width: 420px;
    font-family: "Montserrat", sans-serif; font-weight: 700;
    font-size: 17px; line-height: 1.3; color: var(--ink);
  }
  .order {
    position: absolute; left: 560px; top: 572px; width: 400px;
    color: var(--ink);
  }
  .order .phone-icon { position: absolute; left: 100px; top: -46px; }
  .order .lead { font-size: 18px; line-height: 1.1; }
  .order .number {
    font-family: "Montserrat", sans-serif; font-weight: 800;
    font-size: 36px; line-height: 1.05; letter-spacing: 1px;
  }
  .order .follow { font-size: 18px; line-height: 1.1; }
  .order .web { font-size: 13px; letter-spacing: 4px; margin-top: 6px; }
</style>
</head>
<body>
  <main class="flyer">
    <svg class="yellow-band" viewBox="0 0 1000 680" aria-hidden="true">
      <polygon points="0,450 450,450 520,560 1000,560 1000,680 0,680" fill="var(--accent-yellow)"/>
    </svg>

    <div class="oven-visual" role="img" aria-label="Photo of an open stainless steel built-in oven"></div>

    <div class="brand">
      <div class="name">Pemblo</div>
      <div class="tagline">Simply sizzle</div>
    </div>

    <header class="headline-banner">
      <div class="question">Don't feel like cooking?</div>
      <div class="answer">But feel like a home cooked roast</div>
    </header>

    <div class="dish-photo">
      <div class="fill" role="img" aria-label="Photo of a roast chicken with peppers and onions in a white dish"></div>
    </div>

    <p class="intro">Don't feel like shopping, peeling, chopping, cooking, or cleaning up? We prepare and deliver ready to roast free range chicken and fresh vegetables to your door.</p>

    <p class="no-carbs">No bad carbs!</p>
    <p class="offer">Ready to roast Free range chicken and fresh veggies</p>
    <p class="price price-two">For 2 R99</p>
    <p class="price price-four">For 4 R139</p>

    <p class="ingredients">Only the best ingredients used Free range chickens.<br>Fresh herbs and vegetables. Virgin olive oil.</p>

    <div class="order">
      <svg class="phone-icon" width="40" height="40" viewBox="0 0 40 40" aria-hidden="true">
        <circle cx="20" cy="20" r="17" fill="none" stroke="var(--ink)" stroke-width="3"/>
        <path d="M14 11c-1 0-3 2-3 4 0 7 7 14 14 14 2 0 4-2 4-3l-4-4-3 2c-3-1-6-4-7-7l2-3z" fill="var(--ink)"/>
      </svg>
      <p class="lead">To order SMS your name to</p>
      <p class="number">074 318 6149</p>
      <p class="follow">and we'll call you back.</p>
      <p class="web">www.pemblo.co.za</p>
    </div>
  </main>
</body>
</html>
```